Stationery Design Project

Would like to have the design elements we created in for our website (www.brook-holdings.example), incorporated in a stationery design layout.
Updates
Colors used in the logo attachments do not need to be used. We are open to different color variations. Looking for a crisp, clean, modern update using the design elements in attachments and which can also be viewed on or website.
A note to designers:
Project Deadline Extended
Reason: Due to update in our project description and requirements, we have decided to extend the deadline of this project to provide ample opportunity to all designers participating .
Requirements
Must have
- Must have continuity with the theme and design features used in our website. Have attached .jpg images of some of the design elements.

```html
<!DOCTYPE html>
<html lang="en">
<head>
<meta charset="utf-8">
<title>Brook Holdings Letterhead</title>
<link href="https://fonts.googleapis.com/css2?family=Questrial&display=swap" rel="stylesheet">
<style>
  :root {
    --canvas: #ffffff;
    --sheet: #e2efdb;
    --sheet-edge: #cfd6cc;
    --mark-panel: #e7f1e3;
    --ink: #1a1a1a;
    --mark-ink: #2f3b30;
    --ghost: rgba(150, 156, 148, 0.4);
  }
  * { margin: 0; padding: 0; box-sizing: border-box; }
  html, body { width: 848px; height: 1200px; overflow: hidden; background: var(--canvas); }
  .letterhead {
    position: relative;
    width: 848px;
    height: 1200px;
    overflow: hidden;
    font-family: "Questrial", sans-serif;
  }
  .sheet {
    position: absolute;
    left: 51px;
    top: 51px;
    width: 738px;
    height: 1087px;
    background: var(--sheet);
    border: 1px solid var(--sheet-edge);
  }
  .brand-mark {
    position: absolute;
    left: 336px;
    top: 54px;
    width: 232px;
    height: 130px;
    background: var(--mark-panel);
    display: flex;
    align-items: center;
    justify-content: center;
  }
  .brand-name {
    font-family: "Questrial", sans-serif;
    font-size: 54px;
    font-weight: 400;
    letter-spacing: 2px;
    color: var(--mark-ink);
  }
  .ghost-name {
    position: absolute;
    left: 60px;
    top: 780px;
    font-family: "Questrial", sans-serif;
    font-size: 250px;
    font-weight: 400;
    line-height: 1;
    color: var(--ghost);
    white-space: nowrap;
  }
  .contact {
    position: absolute;
    left: 51px;
    width: 738px;
    top: 1080px;
    text-align: center;
    font-size: 15.5px;
    line-height: 20px;
    color: var(--ink);
  }
  .contact p { white-space: nowrap; }
</style>
</head>
<body>
  <main class="letterhead">
    <div class="sheet"></div>
    <div class="ghost-name" aria-hidden="true">Brook</div>
    <header class="brand-mark">
      <span class="brand-name">Brook</span>
    </header>
    <footer class="contact">
      <p>This is where address and contact details will align. studio@brook-holdings.example</p>
      <p>cell: 000 555 0142</p>
    </footer>
  </main>
</body>
</html>
```